new member announcement flyer

We need a flyer announcing new members. the content is in attached files. Interested in designs with one, two or four announcements on a 8.5x11 standard sheet. Our website is www.gearlotnet.com

Font styles to use
Sans Serif

```html
<!DOCTYPE html>
<html lang="en">
<head>
<meta charset="utf-8">
<title>GearLotNet – New Member Announcement</title>
<link rel="stylesheet" href="https://fonts.googleapis.com/css2?family=Open+Sans:wght@400;700&display=swap">
<style>
  :root {
    --ink-dark: #2b2b2b;
    --band-blue: #3874ab;
    --band-red: #aa2424;
    --band-red-edge: #7d1515;
    --text-body: #333333;
    --text-muted: #6f7780;
    --icon-blue: #3b78b3;
    --white: #ffffff;
    --photo-dark: #3a2b24;
    --photo-warm: #7a5a44;
  }
  html, body { margin: 0; padding: 0; overflow: hidden; background: var(--white); }
  .flyer {
    position: relative; width: 1200px; height: 938px; overflow: hidden;
    background: var(--white);
    font-family: "Open Sans", Arial, sans-serif;
  }
  .hero-photo {
    position: absolute; left: 0; top: 0; width: 1200px; height: 83px;
    background: linear-gradient(90deg, var(--photo-dark) 0%, var(--photo-warm) 35%, #5e4536 60%, var(--photo-warm) 85%, var(--photo-dark) 100%);
  }
  .hero-bar {
    position: absolute; left: 267px; top: -8px; width: 675px; height: 12px;
    background: var(--band-blue); border-radius: 6px;
  }
  .bands { position: absolute; left: 0; top: 0; }
  .products-title {
    position: absolute; left: 37px; top: 167px; margin: 0;
    color: var(--white); font-weight: 400; font-size: 32.5px; letter-spacing: 2.2px; line-height: 1.2;
  }
  .product-list { list-style: none; margin: 0; padding: 0; }
  .product-list li {
    position: absolute; color: var(--white); font-size: 24px; letter-spacing: 1.6px;
    line-height: 1; transform: translateY(-50%);
  }
  .product-list li::before { content: "\2022"; margin-right: 10px; font-size: 18px; vertical-align: 3px; }
  .focus-title {
    position: absolute; left: 37px; top: 328px; margin: 0;
    color: var(--white); font-weight: 700; font-size: 47px; letter-spacing: 3.7px; line-height: 1;
  }
  .focus-body {
    position: absolute; left: 35px; top: 436px; width: 720px; margin: 0;
    color: var(--text-body); font-size: 20.5px; letter-spacing: 1.27px; line-height: 39.75px;
  }
  .contact { position: absolute; left: 845px; top: 0; }
  .contact-row { position: absolute; left: 0; white-space: nowrap; }
  .contact-row svg { position: absolute; left: 8px; }
  .contact-label {
    position: absolute; left: 30px; color: var(--text-muted); font-size: 22.5px; letter-spacing: 1.4px; line-height: 1;
  }
  .contact-value {
    position: absolute; left: 143px; color: var(--text-muted); font-size: 12px; letter-spacing: 0.6px; line-height: 15px;
  }
  .footer {
    position: absolute; left: 0; top: 781px; width: 1200px; height: 157px;
    background: var(--ink-dark); color: var(--white);
    font-size: 20.5px; letter-spacing: 1.3px; line-height: 30px;
  }
  .footer-address { position: absolute; left: 40px; top: 32px; margin: 0; font-style: normal; text-align: center; }
  .footer-numbers { position: absolute; left: 887px; top: 32px; margin: 0; }
</style>
</head>
<body>
<div class="flyer">
  <div class="hero-photo" role="img" aria-label="Close-up photograph of an electronic circuit board"></div>
  <div class="hero-bar"></div>

  <svg class="bands" width="1200" height="420" viewBox="0 0 1200 420" aria-hidden="true">
    <rect x="0" y="82.5" width="1200" height="211" fill="var(--band-blue)"/>
    <polygon points="0,82.5 412.5,82.5 475.3,190.3 412.5,293.4 0,293.4" fill="var(--ink-dark)"/>
    <polygon points="0,297 689,297 689,409.7 0,409.7" fill="var(--band-red-edge)"/>
    <polygon points="0,293.4 695.6,293.4 751.9,345.9 692,406 0,406" fill="var(--band-red)"/>
  </svg>

  <h2 class="products-title">PRODUCTS OFFERING</h2>
  <ul class="product-list">
    <li style="left:719px; top:110px">Transistors</li>
    <li style="left:571px; top:151px">Capacitors</li>
    <li style="left:907px; top:151px">Relays</li>
    <li style="left:571px; top:208px">Connectors</li>
    <li style="left:907px; top:208px">Crystals</li>
    <li style="left:571px; top:265px">Diodes</li>
    <li style="left:907px; top:265px">Resistors</li>
  </ul>

  <h1 class="focus-title">CLASSIFICATION FOCUS</h1>
  <p class="focus-body">Global Leader in Semiconductor and electronic Component<br>distributionThis is our studio's versionof Lorem Ipsum. Proin<br>gravida nibh vel velit auctor aliquetAenean sollicitudin, lorem<br>quis bibendum auctor, nisi elitconsequat ipsum, nec sagittis<br>sem nibh id elit. Duis sed odiosit amet nibh vulputate cursus a<br>sit amet mauris. Morbi accumsanipsum velit. Nam nec tellus a<br>odio tincidunt auctor a ornare odio.Sed non&nbsp; mauris vitae erat<br>&nbsp;consequat auctor eu in elit. Class aptentt</p>

  <div class="contact">
    <div class="contact-row" style="top:476px">
      <svg width="18" height="22" viewBox="0 0 18 22"><path d="M9 0C4.6 0 1.5 3.3 1.5 7.4 1.5 12.6 9 21 9 21s7.5-8.4 7.5-13.6C16.5 3.3 13.4 0 9 0zm0 10.2a2.9 2.9 0 1 1 0-5.8 2.9 2.9 0 0 1 0 5.8z" fill="var(--icon-blue)"/></svg>
      <span class="contact-label" style="top:0">Location</span>
      <span class="contact-value" style="top:5px">77 Cedar Ridge Ln Westbrook,<br>CA 90412</span>
    </div>
    <div class="contact-row" style="top:525px">
      <svg width="22" height="22" viewBox="0 0 22 22" style="top:0"><circle cx="11" cy="11" r="9.5" fill="none" stroke="var(--icon-blue)" stroke-width="1.6"/><path d="M7.6 6.3l1.7-.3 1 2.4-1.1.9c.6 1.3 1.5 2.2 2.8 2.8l.9-1.1 2.4 1-.3 1.7c-3.9.3-7.7-3.5-7.4-7.4z" fill="var(--icon-blue)"/></svg>
      <span class="contact-label" style="top:0">Phone</span>
      <span class="contact-value" style="top:5px">555-302-7741</span>
    </div>
    <div class="contact-row" style="top:570px">
      <svg width="20" height="16" viewBox="0 0 20 16" style="top:3px"><rect x="0" y="0" width="20" height="16" rx="1.5" fill="var(--icon-blue)"/><path d="M1 1.5l9 7 9-7" fill="none" stroke="var(--white)" stroke-width="1.6"/></svg>
      <span class="contact-label" style="top:0">Email</span>
      <span class="contact-value" style="top:5px">sales@voltrimparts.com</span>
    </div>
  </div>

  <footer class="footer">
    <address class="footer-address">GearLotNet. Inc<br>412 Harbor Vale Road<br>Fairmont, FL 33901</address>
    <p class="footer-numbers">Phone : (555) 214-0700<br>Fax : (555) 214-0795<br>Toll Free : (800) 555-0148</p>
  </footer>
</div>
</body>
</html>
```